Oral Surgeon Referral Pads

Hello. We need referral pads for Dr Loretta Pembrooke, DDS board certified oral surgeon's new office - Cedar Hollow Oral & Maxillofacial Surgery. See logo uploaded. See some images we would like included
Updates

Designs look the same

Font styles to use
Serif
Script

Colors
00AB8E
00BBA5
67D7C9
C6EFE9
E9F9F6

Requirements
Must have
• Color Pantone 623c. Also foldable business cards

```html
<!DOCTYPE html>
<html lang="en">
<head>
<meta charset="utf-8">
<title>Cedar Hollow Oral &amp; Maxillofacial Surgery – Referral Pad</title>
<link rel="stylesheet" href="https://fonts.googleapis.com/css2?family=Open+Sans:wght@400;500;600;700&family=Lora:wght@400&display=swap">
<style>
  :root {
    --stage: #606060;
    --paper: #ffffff;
    --navy: #232f6b;
    --ink: #2b2b2b;
    --chart-fill: #eaf2f8;
    --chart-edge: #a9c6de;
    --tissue-fill: #f1f2f4;
  }
  * { box-sizing: border-box; margin: 0; padding: 0; }
  html, body { width: 1200px; height: 1004px; overflow: hidden; }
  body {
    background: var(--stage);
    font-family: "Open Sans", Arial, sans-serif;
    color: var(--ink);
    position: relative;
  }
  .pad {
    position: absolute;
    background: var(--paper);
    box-shadow: 0 4px 10px rgba(0,0,0,.35);
  }
  .pad--front { left: 127px; top: 159px; width: 455px; height: 683px; }
  .pad--back  { left: 615px; top: 158px; width: 458px; height: 686px; }
  .pad__band {
    position: absolute; left: 0; right: 0; bottom: 0; height: 14px;
    background: var(--navy);
  }
  .abs { position: absolute; white-space: nowrap; }

  /* front */
  .doctor { left: 26px; top: 32px; font-size: 13px; font-weight: 700; color: var(--navy); }
  .contact { left: 26px; font-size: 10.5px; display: flex; align-items: center; gap: 3px; line-height: 1; }
  .contact svg { width: 9px; height: 9px; fill: var(--navy); }
  .brand {
    left: 210px; top: 72px; width: 222px; text-align: center;
    font-family: "Lora", Georgia, serif; font-weight: 400; color: var(--navy);
  }
  .brand__name { font-size: 25px; line-height: 1.1; }
  .brand__tag { font-size: 13.5px; margin-top: 4px; }
  .field { left: 27px; font-size: 10.5px; }
  .rule { position: absolute; left: 27px; width: 401px; height: 1.5px; background: var(--navy); }
  .date span { margin-left: 14px; }
  .note { left: 27px; top: 331px; font-size: 10.3px; }
  .tooth-chart {
    position: absolute; left: 27px; top: 371px; width: 245px; height: 128px;
    background: var(--chart-fill); border: 2px solid var(--chart-edge);
  }
  .tissue-chart {
    position: absolute; left: 27px; top: 510px; width: 377px; height: 142px;
    background: var(--tissue-fill);
  }

  /* back */
  .label { left: 54px; font-size: 11.5px; font-weight: 500; }
  .label--caps { font-size: 9.5px; }
  .check { display: flex; align-items: center; gap: 5px; font-size: 11.3px; font-weight: 500; line-height: 1; }
  .check::before {
    content: ""; width: 6px; height: 6px; border: 1.4px solid var(--navy); flex: none;
  }
  .check--small { font-size: 9.5px; font-weight: 400; }
  .blank { position: absolute; height: 1px; background: var(--navy); }
  .sketch-box {
    position: absolute; left: 29px; top: 372px; width: 402px; height: 269px;
    border: 3px solid var(--navy);
  }
</style>
</head>
<body>

<section class="pad pad--front">
  <p class="abs doctor">Dr Loretta Pembrooke</p>

  <p class="abs contact" style="top:91px"><svg viewBox="0 0 10 10"><path d="M5 0a3.5 3.5 0 0 0-3.5 3.5C1.5 6 5 10 5 10s3.5-4 3.5-6.5A3.5 3.5 0 0 0 5 0zm0 5a1.4 1.4 0 1 1 0-2.8A1.4 1.4 0 0 1 5 5z"/></svg>Your address, City State, Zip 1234</p>
  <p class="abs contact" style="top:107px"><svg viewBox="0 0 10 10"><path d="M2 0l2 2.5-1 1.2c.6 1.3 1.6 2.3 2.9 2.9l1.2-1L10 7.7 8.6 10C4 9.6.4 6 0 1.4z"/></svg>123 456 789</p>
  <p class="abs contact" style="top:123px"><svg viewBox="0 0 10 10"><path d="M1 3h8v6H1zM2.5 0h5v2.5h-5zM3 5h1v1H3zm2 0h1v1H5zm2 0h1v1H7zM3 7h1v1H3zm2 0h1v1H5zm2 0h1v1H7z"/></svg>123 456 789</p>
  <p class="abs contact" style="top:139px"><svg viewBox="0 0 10 10"><path d="M0 2h10v7H0zm1 1l4 3 4-3"/></svg>info@cedarhollowoms.com</p>

  <div class="abs brand">
    <p class="brand__name">Cedar Hollow</p>
    <p class="brand__tag">Oral &amp; Maxillofacial Surgery</p>
  </div>

  <p class="abs field date" style="top:157px">Today’ s Date<span>DD</span><span>/</span><span>MM</span><span>/</span><span>YYY</span></p>
  <div class="rule" style="top:180px"></div>
  <p class="abs field" style="top:191px">Patient’ s Name</p>
  <div class="rule" style="top:210px"></div>
  <p class="abs field" style="top:217px">Patient’ Phone Number</p>
  <div class="rule" style="top:238px"></div>
  <p class="abs field" style="top:243px">Referred by</p>
  <div class="rule" style="top:263px"></div>
  <p class="abs field" style="top:271px">Additional Comments</p>

  <p class="abs note">You can save time by going online.Register and update your health today</p>

  <div class="tooth-chart" role="img" aria-label="Numbered dental chart of teeth 1 to 32, upper and lower arches, right and left"></div>
  <div class="tissue-chart" role="img" aria-label="Soft tissue chart with two open-mouth oral cavity diagrams"></div>

  <div class="pad__band"></div>
</section>

<section class="pad pad--back">
  <p class="abs label label--caps" style="top:52px">PROCEDURE</p>
  <p class="abs check check--small" style="left:55px;top:72px">Extraction</p>
  <p class="abs check check--small" style="left:130px;top:71px">Implants</p>
  <p class="abs check check--small" style="left:207px;top:72px">Consultation</p>
  <p class="abs check check--small" style="left:288px;top:71px">Radiogrphs</p>

  <p class="abs check" style="left:21px;top:102px">Wisdom Teeth</p>
  <p class="abs check" style="left:21px;top:118px">Extraction</p>
  <p class="abs check" style="left:21px;top:134px">Implants</p>
  <p class="abs check" style="left:21px;top:150px">Bone Grafing</p>
  <p class="abs check" style="left:21px;top:165px">Exposure and bonding</p>
  <p class="abs check" style="left:21px;top:181px">Biopsy(SOFT or Hard Tissue)</p>

  <p class="abs check" style="left:206px;top:102px">Lesion Evaluation</p>
  <p class="abs check" style="left:206px;top:118px">Infection (I&amp;D</p>
  <p class="abs check" style="left:206px;top:134px">Alveoloplasty</p>
  <p class="abs check" style="left:206px;top:150px">Frenectomy</p>
  <p class="abs check" style="left:206px;top:165px">Orthognathic</p>
  <p class="abs check" style="left:206px;top:181px">TMJ</p>
  <p class="abs check" style="left:206px;top:197px">Other</p>
  <div class="blank" style="left:218px;top:217px;width:62px"></div>
  <div class="blank" style="left:218px;top:232px;width:62px"></div>

  <p class="abs check" style="left:321px;top:102px;font-size:11.3px">Implants</p>
  <style>.pad--back .check[style*="left:321px"]::before{display:none}</style>
  <p class="abs check" style="left:311px;top:117px">Alderstone</p>
  <p class="abs check" style="left:311px;top:133px">Osteline</p>
  <p class="abs check" style="left:311px;top:149px">Other</p>
  <div class="blank" style="left:324px;top:171px;width:62px"></div>
  <div class="blank" style="left:324px;top:188px;width:62px"></div>

  <p class="abs label" style="top:238px">Surgical Template</p>
  <p class="abs check" style="left:21px;top:256px">To be provided by Restorative dentist</p>
  <p class="abs check" style="left:255px;top:256px">To be fabricated by the surgeon</p>
  <p class="abs check" style="left:21px;top:272px">Other</p>
  <div class="blank" style="left:83px;top:283px;width:151px"></div>

  <p class="abs label" style="top:299px">Radfographs</p>
  <p class="abs check" style="left:21px;top:315px">Being Mafled/emafled</p>
  <p class="abs check" style="left:163px;top:315px">Given to the Patient</p>
  <p class="abs check" style="left:305px;top:315px">Please Take</p>
  <p class="abs check" style="left:21px;top:331px">Other</p>
  <div class="blank" style="left:83px;top:341px;width:151px"></div>

  <div class="sketch-box"></div>

  <div class="pad__band"></div>
</section>

</body>
</html>
```